Maple Hearth Services Management

I have 4 different restaurant concepts and would like to make a company profile/catalogue for it to be all combined in one. I will provide the description and photos for each restaurant concept. I would like for the catalogue to include:

Cover Page

Over all Introduction page

Concept 1 title page - Sir.Lobster Restaurant
Concept 1 description page
Concept 1 food/restaurant photo page

Concept 2 title page - Dar Halim Restaurant
Concept 2 description page
Concept 2 food/restaurant photo page
Concept 2 outlets/branches page

Concept 3 title page - La Focaccia Restaurant
Concept 3 description page
Concept 3 food/restaurant photo page

Concept 4 title page - El Oud Restaurant & Lounge
Concept 4 description page
Concept 4 food/restaurant photo page

Contact details page

Industry/Entity Type

Restaurant

```html
<!DOCTYPE html>
<html lang="en">
<head>
<meta charset="utf-8">
<title>Maple Hearth Services Management – Restaurant Catalogue Cover</title>
<link href="https://fonts.googleapis.com/css2?family=Oswald:wght@300;600&display=swap" rel="stylesheet">
<style>
  :root {
    --backdrop: #e9e6e2;
    --page-black: #000000;
    --brand-yellow: #f6d21e;
    --band-dark: #262626;
    --text-white: #ffffff;
    --text-ink: #141414;
    --mark-grey: #7a7370;
  }
  html, body {
    margin: 0;
    padding: 0;
    width: 1200px;
    height: 900px;
    overflow: hidden;
    background: var(--backdrop);
    font-family: "Oswald", "Arial Narrow", sans-serif;
  }
  .spread {
    position: absolute;
    left: 50px;
    top: 251px;
    width: 1100px;
    height: 397px;
    display: flex;
    box-shadow: 0 10px 24px rgba(0,0,0,0.35);
  }
  .page {
    position: relative;
    width: 550px;
    height: 397px;
    overflow: hidden;
  }
  .page--back {
    background: var(--page-black);
  }
  .back-photo {
    position: absolute;
    left: 0;
    right: 0;
    bottom: 0;
    height: 140px;
    background:
      radial-gradient(ellipse at 30% 70%, rgba(92,70,36,0.55), transparent 60%),
      radial-gradient(ellipse at 70% 60%, rgba(46,62,30,0.55), transparent 55%),
      linear-gradient(to bottom, rgba(0,0,0,1) 0%, rgba(40,30,18,0.9) 60%, rgba(60,44,26,0.9) 100%);
  }
  .brand-name {
    position: absolute;
    display: flex;
    align-items: center;
    gap: 10px;
    font-weight: 600;
    font-size: 30px;
    letter-spacing: 1px;
    white-space: nowrap;
    transform: translateX(-50%);
  }
  .brand-name__dot {
    width: 14px;
    height: 14px;
    border-radius: 50%;
    background: currentColor;
  }
  .page--back .brand-name {
    left: 274px;
    top: 176px;
    color: var(--mark-grey);
  }
  .page--cover {
    background: #333;
  }
  .cover-photo {
    position: absolute;
    inset: 0;
    background:
      radial-gradient(ellipse at 20% 20%, rgba(170,170,178,0.7), transparent 45%),
      radial-gradient(ellipse at 60% 35%, rgba(120,70,45,0.9), transparent 50%),
      radial-gradient(ellipse at 25% 60%, rgba(150,85,55,0.95), transparent 45%),
      radial-gradient(ellipse at 55% 85%, rgba(220,150,80,0.85), transparent 45%),
      linear-gradient(160deg, #7d7a80 0%, #6b4a3a 40%, #8c5a3c 70%, #b37a4a 100%);
  }
  .frame-bar {
    position: absolute;
    background: var(--brand-yellow);
  }
  .frame-bar--top { left: 232px; top: 0; width: 318px; height: 10px; }
  .frame-bar--right { right: 0; top: 0; width: 12px; height: 77px; }
  .frame-bar--left { left: 0; top: 320px; width: 10px; height: 77px; }
  .frame-bar--bottom { left: 0; bottom: 0; width: 315px; height: 10px; }
  .page--cover .brand-name {
    left: 380px;
    top: 174px;
    color: var(--text-white);
  }
  .title-band {
    position: absolute;
    right: 0;
    display: flex;
    align-items: center;
    justify-content: center;
    text-transform: uppercase;
    line-height: 1;
  }
  .title-band--primary {
    left: 213px;
    top: 249px;
    height: 52px;
    background: var(--band-dark);
    color: var(--text-white);
    font-weight: 600;
    font-size: 46px;
    letter-spacing: 0.5px;
  }
  .title-band--secondary {
    left: 234px;
    top: 301px;
    height: 54px;
    background: var(--brand-yellow);
    color: var(--text-ink);
    font-weight: 300;
    font-size: 46px;
  }
</style>
</head>
<body>
  <main class="spread">
    <section class="page page--back">
      <div class="back-photo" role="img" aria-label="Dimmed photo of a plated salad with greens and roasted vegetables"></div>
      <div class="brand-name"><span class="brand-name__dot"></span>Maple Hearth</div>
    </section>
    <section class="page page--cover">
      <div class="cover-photo" role="img" aria-label="Photo of sausages and steaks on a smoking barbecue grill with tongs"></div>
      <div class="frame-bar frame-bar--top"></div>
      <div class="frame-bar frame-bar--right"></div>
      <div class="frame-bar frame-bar--left"></div>
      <div class="frame-bar frame-bar--bottom"></div>
      <div class="brand-name"><span class="brand-name__dot"></span>Maple Hearth</div>
      <h1 class="title-band title-band--primary" style="margin:0">Restaurant</h1>
      <p class="title-band title-band--secondary" style="margin:0">Catalouge</p>
    </section>
  </main>
</body>
</html>
```